Home web page re-vamp

I would like a stylish new home page design for a clients website.
I have included a sitemap to give some guidance.
The site needs to show off the design capabilitiesof the client

```html
<!DOCTYPE html>
<html lang="en">
<head>
<meta charset="utf-8">
<title>Your Company Name – Architects &amp; Designers</title>
<link rel="stylesheet" href="https://fonts.googleapis.com/css2?family=PT+Sans+Narrow:wght@400;700&family=Open+Sans:wght@400;600;700&family=PT+Sans:wght@700&display=swap">
<style>
:root{
  --navy:#0f2a6e;
  --royal:#1442a6;
  --topbar:#3b5c8f;
  --ink-blue:#1c4f93;
  --nav-text:#2f5a94;
  --cream:#f1eee7;
  --card:#f8f7f4;
  --card-text:#444;
  --green:#93bc35;
  --green-date:#7fae2a;
  --footer:#454545;
  --white:#fff;
}
*{margin:0;padding:0;box-sizing:border-box}
html,body{width:741px;height:1200px;overflow:hidden}
body{position:relative;background:var(--cream);font-family:"Open Sans",Arial,sans-serif;color:#333}
.abs{position:absolute}
.narrow{font-family:"PT Sans Narrow","Arial Narrow",sans-serif}

/* header */
.hero{left:0;top:0;width:741px;height:386px;background:linear-gradient(160deg,#1a3fa0 0%,#3f6fd0 30%,#c9d7ef 50%,#f4e9b5 56%,#4a78d4 70%,#1d44a8 100%)}
.topbar{left:0;top:0;width:741px;height:17px;background:var(--topbar)}
.topbar-call{right:30px;top:3px;font-size:8.5px;color:var(--white)}
.navband{left:0;top:17px;width:741px;height:31px;background:rgba(255,255,255,.82)}
.logo-box{left:62px;top:0;width:158px;height:48px;background:rgba(255,255,255,.9)}
.logo{left:87px;top:17px;font-family:"Open Sans",sans-serif;font-weight:700;font-size:14.5px;letter-spacing:.5px;color:var(--nav-text)}
.main-nav{left:253px;top:27px;display:flex;gap:0;font-size:8px;color:var(--nav-text)}
.main-nav span{margin-right:21px}

.hero-panel{left:199px;top:167px;width:372px;height:96px;border:3px solid rgba(255,255,255,.55);background:rgba(90,110,150,.35)}
.hero-title{left:199px;top:187px;width:372px;text-align:center;font-family:"PT Sans Narrow",sans-serif;font-weight:700;font-size:18px;color:var(--white)}
.hero-sub{left:199px;top:216px;width:372px;text-align:center;font-family:"PT Sans Narrow",sans-serif;font-size:13px;color:var(--white)}
.hero-btn{left:249px;top:244px;width:266px;height:30px;background:var(--white);border:3px solid var(--navy);text-align:center;line-height:24px;font-family:"PT Sans Narrow",sans-serif;font-size:13.5px;color:var(--navy)}

/* blue band */
.band{left:0;top:569px;width:741px;height:255px;background:var(--royal)}

/* cards */
.card{top:338px;width:134px;height:224px;background:var(--card)}
.card-img{left:9px;top:9px;width:114px;height:87px}
.card-title{left:0;top:108px;width:134px;text-align:center;font-family:"PT Sans Narrow",sans-serif;font-size:17.5px;line-height:22px;color:#333}
.card-text{left:12px;top:165px;width:118px;font-family:"PT Sans Narrow",sans-serif;font-size:11.5px;line-height:15px;color:var(--card-text)}
.card-arrow{right:10px;bottom:8px}
.why-title{color:var(--white)}
.why-text{color:var(--white);left:22px;width:100px}
.why-list{left:88px;top:578px;width:122px;list-style:none;font-size:9.2px;line-height:11.5px;color:var(--white)}
.why-list li{position:relative;padding-left:13px;margin-bottom:11px}
.why-list svg{position:absolute;left:0;top:1px}

.latest-title{left:248px;top:590px;font-family:"PT Sans Narrow",sans-serif;font-size:18px;color:var(--white)}
.latest-name{left:249px;top:634px;font-size:9.5px;font-weight:700;color:var(--white)}
.latest-text{left:248px;top:652px;width:148px;font-size:9.5px;line-height:12px;color:var(--white)}
.latest-text p{margin-bottom:11px}
.latest-arrow{left:380px;top:755px}
.dots{left:340px;top:790px;display:flex;gap:9px}
.dots i{width:10px;height:10px;border-radius:50%;background:var(--white)}
.dots i.off{background:#5a7cc8}
.latest-img{left:410px;top:586px;width:248px;height:226px;border:4px solid #8aa6e4;border-radius:3px;background:linear-gradient(180deg,#0c2a3c 0%,#1c5d80 45%,#2d93c8 75%,#0f3c5c 100%)}

/* testimonials & news */
.section-title{font-family:"PT Sans Narrow",sans-serif;font-size:18.5px;color:var(--ink-blue)}
.t-arrows{left:402px;top:852px;font-size:17px;color:var(--ink-blue);word-spacing:14px}
.bubble{left:98px;top:891px;width:353px;height:107px;background:var(--green);border-radius:14px}
.quote-mark{left:112px;top:897px;font-family:Georgia,serif;font-weight:700;font-size:40px;color:var(--white)}
.quote{left:147px;top:911px;width:290px;font-size:13px;line-height:18px;color:#2e3a14}
.client{left:147px;top:958px;font-size:11px;line-height:14px;color:#e9f3cf}
.news-date{left:483px;top:893px;font-size:11px;font-weight:700;color:var(--green-date)}
.news-text{left:483px;top:913px;width:184px;font-size:9.5px;line-height:12px;color:#333}
.news-more{left:483px;top:975px;font-size:9.5px;font-weight:700;color:#333}

.call-now{left:0;top:1010px;width:741px;text-align:center;font-family:"PT Sans",sans-serif;font-weight:700;font-size:30px;color:var(--ink-blue)}

/* footer */
.footer-line{left:0;top:1054px;width:741px;height:6px;background:var(--royal)}
.footer{left:0;top:1060px;width:741px;height:97px;background:var(--footer)}
.footer-nav{left:155px;top:1081px;display:flex;font-size:8px;color:var(--white)}
.footer-nav span{margin-right:22px}
.social{left:311px;top:1113px;display:flex;gap:4px}
.social i{width:20px;height:20px;border-radius:50%;background:var(--white);display:block}
.copyright{left:0;top:1166px;width:741px;text-align:center;font-size:10.5px;color:#333}
</style>
</head>
<body>

<div class="abs hero" role="img" aria-label="Looking up at glass skyscrapers against a bright blue sky"></div>
<div class="abs topbar"></div>
<div class="abs topbar-call">Call Us Now 1123 456 789</div>
<div class="abs navband"></div>
<div class="abs logo-box"></div>
<div class="abs logo">YOUR LOGO</div>
<nav class="abs main-nav">
  <span>About Us</span><span>Services</span><span>Our Clients</span><span>Gallery</span><span>Healty &amp; Safety</span><span>Specification Sheets</span><span>Contact &nbsp;Us</span>
</nav>

<div class="abs hero-panel"></div>
<div class="abs hero-title">YOUR COMAPY NAME</div>
<div class="abs hero-sub">7 DAYS FROM QUOTATION TO DELIVERY USING THE LATEST TECHNOLOGY</div>
<div class="abs hero-btn">ARCHITECTS &amp; DESIGNERS</div>

<div class="abs band"></div>

<!-- Why us column -->
<svg class="abs" style="left:81px;top:338px" width="134" height="455" viewBox="0 0 134 455">
  <path d="M0 0H134V423L67 455L0 423Z" fill="#0f2a6e"/>
</svg>
<div class="abs card" style="left:81px;background:transparent">
  <div class="abs card-img" role="img" aria-label="Two engineers in hard hats reviewing plans" style="border:2px solid #fff;background:linear-gradient(180deg,#6fb6e4,#3b4a5c)"></div>
  <div class="abs card-title why-title">WHY<br>US</div>
  <div class="abs card-text why-text">7 Days from quotation to delivery using the latest technology</div>
</div>
<ul class="abs why-list">
  <li><svg width="10" height="9" viewBox="0 0 10 9"><path d="M1 5l3 3 5-7" stroke="#fff" stroke-width="2" fill="none"/></svg>Loren text here e look for solutions to complex</li>
  <li><svg width="10" height="9" viewBox="0 0 10 9"><path d="M1 5l3 3 5-7" stroke="#fff" stroke-width="2" fill="none"/></svg>Loren &nbsp;involving the funding of capital</li>
  <li><svg width="10" height="9" viewBox="0 0 10 9"><path d="M1 5l3 3 5-7" stroke="#fff" stroke-width="2" fill="none"/></svg>Loren text Equipment</li>
  <li><svg width="10" height="9" viewBox="0 0 10 9"><path d="M1 5l3 3 5-7" stroke="#fff" stroke-width="2" fill="none"/></svg>Loren text ithin an office environment and then</li>
  <li><svg width="10" height="9" viewBox="0 0 10 9"><path d="M1 5l3 3 5-7" stroke="#fff" stroke-width="2" fill="none"/></svg>Lorne textuild documentation around the solution</li>
</ul>

<div class="abs card" style="left:229px">
  <div class="abs card-img" role="img" aria-label="Blue wireframe architectural model on drawings" style="background:linear-gradient(135deg,#e8e8ec,#8c93c8 50%,#d9dae2)"></div>
  <div class="abs card-title">ARCHITECTS &amp;<br>DESIGNERS</div>
  <div class="abs card-text">Advice on colours and materials Environmental friendly manufacture</div>
  <svg class="abs card-arrow" width="12" height="9" viewBox="0 0 12 9"><path d="M0 0l5 4.5L0 9zM6 0l6 4.5L6 9z" fill="#2a5cc0"/></svg>
</div>
<div class="abs card" style="left:374px">
  <div class="abs card-img" role="img" aria-label="Glasses and calculator on financial papers" style="background:linear-gradient(135deg,#f2f3f5,#b9c6d6 60%,#7aa0c2)"></div>
  <div class="abs card-title">COMMERCIAL<br>FIT OUR COMPANIES</div>
  <div class="abs card-text">Site Surveys and Consultation by our experienced design team</div>
  <svg class="abs card-arrow" width="12" height="9" viewBox="0 0 12 9"><path d="M0 0l5 4.5L0 9zM6 0l6 4.5L6 9z" fill="#2a5cc0"/></svg>
</div>
<div class="abs card" style="left:520px">
  <div class="abs card-img" role="img" aria-label="Business people shaking hands" style="background:linear-gradient(135deg,#c9ccd2,#3a3d48 60%,#1f2129)"></div>
  <div class="abs card-title">AWARDS &amp;<br>ACCREDITATIONS</div>
  <div class="abs card-text">We are continually looking at how we can improve our services</div>
  <svg class="abs card-arrow" width="12" height="9" viewBox="0 0 12 9"><path d="M0 0l5 4.5L0 9zM6 0l6 4.5L6 9z" fill="#2a5cc0"/></svg>
</div>

<!-- Latest project -->
<div class="abs latest-title">LATEST PROJECT</div>
<div class="abs latest-name">Project Name</div>
<div class="abs latest-text">
  <p>Loren text here e look for solutions to complex problems involving the funding of capital equipment</p>
  <p>Within an office environment and then build documentation around the solution</p>
</div>
<svg class="abs latest-arrow" width="13" height="10" viewBox="0 0 13 10"><path d="M0 0l5.5 5L0 10zM6.5 0l6.5 5-6.5 5z" fill="#fff"/></svg>
<div class="abs dots"><i class="off"></i><i></i><i></i></div>
<div class="abs latest-img" role="img" aria-label="Glowing digital city skyline in blue light"></div>

<!-- Testimonials -->
<div class="abs section-title" style="left:87px;top:852px">WHAT PEOPLE SAY ABOUT US</div>
<div class="abs t-arrows">&lt; &gt;</div>
<svg class="abs" style="left:76px;top:907px" width="26" height="22" viewBox="0 0 26 22"><path d="M0 3L26 0V22Z" fill="#93bc35"/></svg>
<div class="abs bubble"></div>
<div class="abs quote-mark">“</div>
<div class="abs quote">...very efficient dealing with all the necessary paperwork and found me the best deals</div>
<div class="abs client">Client name<br>USA ...</div>

<div class="abs section-title" style="left:484px;top:852px">NEWS AND EVENTS</div>
<div class="abs news-date">11 05 2014</div>
<div class="abs news-text">We look for solutions to complex problems involving the funding of capital equipment within an office environment and then build documentation around the solution</div>
<div class="abs news-more">Read More...</div>

<div class="abs call-now">Call Us Now 123 456 789</div>

<footer>
  <div class="abs footer-line"></div>
  <div class="abs footer"></div>
  <nav class="abs footer-nav">
    <span>Home</span><span>About Us</span><span>Services</span><span>Our Clients</span><span>Gallery</span><span>Healty &amp; Safety</span><span>Specification Sheets</span><span>Contact &nbsp;Us</span>
  </nav>
  <div class="abs social">
    <i></i><i></i><i></i><i></i><i></i>
    <svg width="20" height="20" viewBox="0 0 20 20"><circle cx="10" cy="10" r="10" fill="#fff"/><rect x="5" y="6.5" width="10" height="7" fill="none" stroke="#454545" stroke-width="1.3"/><path d="M5 6.5l5 4 5-4" fill="none" stroke="#454545" stroke-width="1.3"/></svg>
  </div>
  <div class="abs copyright">© &nbsp;your company name here &nbsp;All rights reserved.</div>
</footer>

</body>
</html>
```